Residential home builder needs a fresh looking business card

We require a fresh looking business card for our business. We like the clean modern look. I have uploaded out logo and our email footer that incorporates some different elements. Blacks and Whites are good but i will leave this up to the design crowd creative minds.

our slogan is:
your idea of the perfect home

website (temporary site) but similar look and feel to the finished one
pinegrovedwellings.com.au

We also have intentions to apply the same look and feel to the rest of our stationary (letterheads, envelopes, site signs, vehicles etc)

Home Builder

```html
<!DOCTYPE html>
<html lang="en">
<head>
<meta charset="utf-8">
<title>Pine Grove Dwellings – Business Card</title>
<link href="https://fonts.googleapis.com/css2?family=Lato:wght@400;700&display=swap" rel="stylesheet">
<style>
  :root {
    --backdrop: #d9d6d1;
    --card-dark: #232222;
    --card-dark-line: #2f2e2e;
    --card-light: #ececec;
    --ink: #1e1e1e;
    --ink-soft: #444444;
    --gold: #d4a514;
    --band-black: #141414;
  }
  * { box-sizing: border-box; margin: 0; padding: 0; }
  html, body {
    width: 1200px; height: 900px; overflow: hidden;
    background: var(--backdrop);
    font-family: "Lato", Arial, sans-serif;
  }
  .sheet {
    width: 1200px; height: 900px;
    display: flex; flex-direction: column; align-items: center; justify-content: center;
    gap: 40px;
  }
  .card {
    position: relative;
    width: 620px; height: 379px;
    overflow: hidden;
    box-shadow: 0 4px 14px rgba(0,0,0,0.18);
  }

  /* Back side */
  .card-back { background: var(--card-dark); }
  .card-back .plan-texture {
    position: absolute; inset: 0;
    background: linear-gradient(135deg, var(--card-dark) 0%, var(--card-dark-line) 50%, var(--card-dark) 100%);
  }
  .card-back .brand {
    position: absolute; left: 0; right: 0; top: 130px;
    display: flex; justify-content: center; align-items: center; gap: 12px;
  }
  .brand-mark { width: 16px; height: 16px; background: var(--gold); }
  .card-back .brand-name {
    color: #ffffff; font-weight: 700; font-size: 30px; letter-spacing: 1px;
  }
  .card-back .slogan {
    position: absolute; left: 0; right: 0; top: 222px;
    text-align: center; color: var(--gold); font-size: 17px; letter-spacing: 0.5px;
  }

  /* Front side */
  .card-front { background: var(--card-light); }
  .card-front .brand {
    position: absolute; left: 40px; top: 200px;
    display: flex; align-items: center; gap: 10px;
  }
  .card-front .brand-name {
    color: var(--ink); font-weight: 700; font-size: 24px; letter-spacing: 0.5px;
  }
  .holder {
    position: absolute; left: 330px; top: 62px;
  }
  .holder-name { font-size: 22px; font-weight: 700; color: var(--ink); }
  .holder-title { font-size: 12px; color: var(--ink-soft); margin-top: 2px; }
  .contacts {
    position: absolute; left: 330px; top: 150px;
    font-size: 12.5px; color: var(--ink); line-height: 1.55;
  }
  .contacts .group + .group { margin-top: 12px; }
  .contacts .key { color: var(--gold); font-weight: 700; margin-right: 6px; }
  .contacts .gap { margin-left: 10px; }
  .contacts .web { font-weight: 700; }
  .bands { position: absolute; left: 0; bottom: 0; }
</style>
</head>
<body>
<main class="sheet">

  <section class="card card-back" aria-label="Card back">
    <div class="plan-texture" role="img" aria-label="Faint house floor plan line drawing across the dark background"></div>
    <div class="brand">
      <span class="brand-mark"></span>
      <span class="brand-name">Pine Grove Dwellings</span>
    </div>
    <p class="slogan">your idea of the perfect home</p>
  </section>

  <section class="card card-front" aria-label="Card front">
    <div class="brand">
      <span class="brand-mark"></span>
      <span class="brand-name">Pine Grove Dwellings</span>
    </div>

    <div class="holder">
      <p class="holder-name">Marcus Hale</p>
      <p class="holder-title">General Manager</p>
    </div>

    <div class="contacts">
      <div class="group">
        <p><span class="key">M</span>0412 555 019</p>
        <p><span class="key">E</span>marcus@pinegrovedwellings.com.au</p>
      </div>
      <div class="group">
        <p><span class="key">P</span>08 5550 1402<span class="gap"></span><span class="key">F</span>08 5550 1788</p>
        <p>PO Box 4417, Harbour Vale DC, WA 6999</p>
        <p class="web">www.pinegrovedwellings.com.au</p>
      </div>
    </div>

    <svg class="bands" width="620" height="30" viewBox="0 0 620 30" aria-hidden="true">
      <polygon points="0,16 262,16 248,30 0,30" fill="var(--gold)"/>
      <polygon points="420,2 620,2 620,30 396,30" fill="var(--band-black)"/>
    </svg>
  </section>

</main>
</body>
</html>
```